Web-page design

We need a initial web design for our page kelbrook.com.au (which is not yet set up).
We provide consulting services for all kinds of problems in and between organisations.
Main focus is on conflict resolution but we also support companies on improving their operational performance.
We want to have the following page structure (and part of the project is to design the 8 pages):
- Home
- Services (we offer 3 main service areas - one per page)
- Case studies (one per page)
- Engaging us (our process)
- About Conflict & low performance
- Conflict resolution App
- About
- Contact (Email form)
- Our logo should be on each page.
The start page should include the following information:
- Twitter / Linkedin / facebook/ google + Links
- Telephone / Email or in general contact details
- News
- A quite prominent picture box with 3 alternating pics - each representing one of our service areas
- Link to our App
- Testimonials
It would be nice if the service pages would have an image header. Links to the information section (about conflict & low performance; and the app page) would be nice as well.
We like the following joomla designs: www.frandelthemes.com/itempreview/153
No need to copy it, it should just give you an idea.
We like the layout here with the picture and space for the case studies on the left. Somewhere beneath should be the 3 service areas with a picture each.
In terms of colors: our logo colours are Blue (RBG 8;44;80) and Orange (RGB 231;120;23). The orange could be used to emphasise certain things, however there should not be too much color.
Budget for images available, so please use placeholders or ask us for specific photos/images, if you need them for your design.
Updates
Hi, one more thing that we would like to have is the case studies not hidden behind a link "case studies" - we would like to have them individually linked prominent on the first page. There will be about 6-8 of them. Thats what we liked on the joomla template (the links left from the picture).
Hi, thanks very much for all the great proposals.
We are currently going through the selection process and will post our decision early next week.
Thanks again!
Wilma
Target Market(s)
- target customers are all different kinds of businesses and organisations (all industries, government, non-for-profit, ...) experiencing conflict and tension - be it with internal staff, amongst managers or board members, dysfunctional teams, between organizations or customers and organizations... examples could be bullying allegations, governmental negotiations with unions, disputes within organizations etc.
- also we will offer performance improvement services for organizations
- we will offer mediation, facilitation, negotiation, performance improvement services, conflict coaching, conflict management, change management services
- if comparable to anything - then to a law firm in terms of dealing with conflicts but its much less adversarial and much more about the people and their interests rather than about laws
- basically it's all kind of things you can do in order to solve disputes without involving lawyers and a court - so it's much cheaper and target is to find a solution all parties can live with rather than having a judge deciding about who wins and who looses
- performance management is more about analysing reasons for a lack of performance and setting up continous improvement systems, supporting change management, facilitating improvement workshops or strategic meetings, ...
Industry/Entity Type
Consulting
Look and feel

```html
<!DOCTYPE html>
<html lang="en">
<head>
<meta charset="utf-8">
<title>Kelbrook Mediation</title>
<link rel="stylesheet" href="https://fonts.googleapis.com/css2?family=Open+Sans:wght@400;600;700&family=PT+Sans:wght@400;700&display=swap">
<style>
:root{
  --navy:#082c50;
  --orange:#e77817;
  --ink:#444;
  --muted:#888;
  --panel:#123a66;
  --footer:#0b1626;
  --footer-line:#2a3648;
  --card-head:#5b5b5b;
  --teal:#2a93ad;
  --green:#8cb833;
  --amber:#e8912a;
  --red:#d9542f;
}
*{box-sizing:border-box;margin:0;padding:0}
html,body{width:1174px;height:1200px;overflow:hidden;background:#fff}
body{font-family:"Open Sans",sans-serif;color:var(--ink)}
.page{position:relative;width:1200px;height:1227px;transform:scale(0.9783);transform-origin:0 0}
.abs{position:absolute}
ul{list-style:none}

.topbar{left:0;top:0;width:1200px;height:25px;background:linear-gradient(#fafafa,#ececec);border-bottom:1px solid #e0e0e0}
.topbar-link{top:6px;font-size:11px;color:#8a8a8a;text-transform:uppercase}
.topbar-link::before{content:"";display:inline-block;width:10px;height:10px;border:1.5px solid #999;border-radius:2px;margin-right:7px;vertical-align:-1px}

.logo{left:111px;top:55px;display:flex;align-items:center;gap:10px}
.logo-name{font-family:"PT Sans",sans-serif;font-size:27px;color:var(--navy);letter-spacing:1px}
.logo-mark{width:22px;height:22px;background:var(--orange)}
.logo-url{left:134px;top:93px;font-size:10px;letter-spacing:7.4px;color:var(--navy);font-weight:700}

.nav{left:477px;top:70px;display:flex;gap:0;font-family:"PT Sans",sans-serif;font-weight:700;font-size:12.5px;color:#444;text-transform:uppercase}
.nav li{margin-right:32px}
.nav li:last-child{margin-right:0}
.nav .has-sub::after{content:"›";margin-left:6px;color:#777}
.nav-shadow{left:477px;top:96px;width:613px;height:6px;background:linear-gradient(rgba(0,0,0,.05),transparent)}

.hero-band{left:0;top:119px;width:1200px;height:332px;background:#f1f2f3}
.cases{left:110px;top:119px;width:245px;height:332px;background:linear-gradient(160deg,#1d4c82,#0c2a4e)}
.cases-title{left:131px;top:139px;width:207px;height:30px;background:#fff;box-shadow:0 2px 3px rgba(0,0,0,.35);color:var(--orange);font-family:"PT Sans",sans-serif;font-size:16px;font-weight:700;padding:5px 12px}
.cases-list{left:136px;top:193px;font-family:"PT Sans",sans-serif;font-size:13px;color:#fff;text-transform:uppercase}
.cases-list li{height:23px;line-height:19px}
.cases-list li::before{content:"›";font-size:15px;margin-right:11px}
.hero-photo{left:355px;top:119px;width:735px;height:332px;background:linear-gradient(100deg,#c9ccd2 0%,#e6e3df 30%,#7e8796 55%,#d8dbe0 80%,#eef0f2 100%)}
.caption{left:841px;top:167px;width:231px;height:246px;background:rgba(38,68,108,.9);border-radius:4px;color:#fff;padding:20px 18px 0 21px}
.caption::before{content:"";position:absolute;left:-8px;top:27px;border:8px solid transparent;border-right:0;border-left:10px solid var(--orange);left:-3px}
.caption h2{font-family:"PT Sans",sans-serif;font-weight:400;font-size:26px;line-height:30px;margin-bottom:11px}
.caption p{font-size:13px;line-height:18px}
.dots{left:399px;top:403px;width:74px;height:20px;background:rgba(0,0,0,.18);border-radius:10px;display:flex;align-items:center;gap:11px;padding-left:12px}
.dots span{width:6px;height:6px;border-radius:50%;background:#ddd}
.dots span.on{width:11px;height:11px;border:2px solid #fff;background:transparent}

.card{top:489px;width:229px;height:323px;background:linear-gradient(#fff 60%,#f6f6f6);border-bottom:4px solid #e2e2e2}
.card-head{height:37px;background:var(--card-head);color:#fff;font-family:"PT Sans",sans-serif;font-weight:700;font-size:14.5px;padding:9px 12px;text-transform:uppercase;border-bottom:3px solid}
.card-head::before{content:"";position:absolute;left:0;top:13px;border:5px solid transparent;border-left:5px solid #fff}
.card-img{position:absolute;left:13px;top:57px;width:200px;height:89px}
.card-text{position:absolute;left:12px;top:158px;width:200px;font-size:12.5px;line-height:17px;color:#555}
.card-dots{position:absolute;left:13px;top:249px;width:50px;border-top:1px dotted #555}
.more{position:absolute;left:8px;top:273px;width:98px;height:24px;border-radius:12px;background:#fff;box-shadow:0 1px 3px rgba(0,0,0,.25);font-size:11px;color:var(--orange);padding:4px 0 0 13px}
.more::after{content:"+";position:absolute;right:9px;top:5px;width:12px;height:12px;border:1.5px solid var(--orange);border-radius:50%;font-size:10px;line-height:9px;text-align:center;font-weight:700}

.clients{left:0;top:877px;width:1200px;height:102px;background:#f3f3f3;border-top:1px solid #ddd}
.clients-tab{left:110px;top:863px;width:340px;height:26px;background:#fff;box-shadow:0 1px 2px rgba(0,0,0,.15);font-size:12.5px;color:#333;padding:5px 0 0 8px}
.clients-tab a{color:var(--orange);text-decoration:underline;margin-left:10px}
.client-names{left:112px;top:924px;width:975px;display:flex;justify-content:space-between;font-family:"PT Sans",sans-serif;font-weight:700;font-size:26px;color:#8d8d8d}

.footer{left:0;top:979px;width:1200px;height:248px;background:var(--footer)}
.news-title{left:113px;top:1007px;font-family:"PT Sans",sans-serif;font-size:21px;color:#fff}
.news-text{left:113px;top:1034px;width:220px;font-size:12.5px;line-height:17px;color:#9aa3af}
.news-form{left:111px;top:1082px;width:224px;height:34px;background:#fff;border:1px solid #ccc;border-radius:3px;font-size:12.5px;color:#888;padding:8px 10px}
.news-btn{position:absolute;right:2px;top:2px;width:31px;height:28px;background:#555;border-radius:2px}
.vrule{top:997px;width:1px;height:143px;background:var(--footer-line)}
.foot-links{left:410px;top:1000px;font-family:"PT Sans",sans-serif;font-size:12.5px;color:#fff;text-transform:uppercase}
.foot-links li{height:21px}
.foot-links li::before,.foot-cases::before{content:"›";font-size:15px;color:#aaa;margin-right:8px}
.foot-cases{left:568px;top:1000px;font-family:"PT Sans",sans-serif;font-size:12.5px;color:#fff}
.foot-sub{top:1026px;font-size:11px;color:#8c96a3}
.foot-sub li{height:18px}
.office{right:115px;top:997px;text-align:right;font-family:"PT Sans",sans-serif;color:#fff;font-size:13px;line-height:18px}
.office .org{color:var(--orange);font-size:14.5px;line-height:20px}
.office .hq{color:var(--orange);font-size:14.5px;margin-bottom:10px}
.office .sep{display:inline-block;width:38px;border-top:1px dotted #888;margin:0 0 20px}
.hline{left:110px;top:1160px;width:980px;height:1px;background:var(--footer-line)}
.legal{left:113px;top:1185px;font-size:11px;color:#aaa}
.legal a{color:var(--orange);text-decoration:none}
.legal .bar{margin:0 12px;color:#888}
.follow{right:111px;top:1183px;display:flex;align-items:center;gap:9px;font-size:11.5px;color:#888}
.follow span.dot{width:25px;height:25px;border-radius:50%;background:#555c66}
</style>
</head>
<body>
<div class="page">

  <div class="abs topbar"></div>
  <span class="abs topbar-link" style="left:884px">Apply now</span>
  <span class="abs topbar-link" style="left:1006px">Contact us</span>

  <div class="abs logo"><span class="logo-name">KELBROOK MEDIATION</span><span class="logo-mark"></span></div>
  <div class="abs logo-url">www.kelbrook.com.au</div>

  <ul class="abs nav">
    <li class="has-sub">Services</li>
    <li class="has-sub">Case Studies</li>
    <li>Engaging us</li>
    <li>About Conflict</li>
    <li class="has-sub">Conflict App</li>
    <li>About us</li>
  </ul>
  <div class="abs nav-shadow"></div>

  <div class="abs hero-band"></div>
  <div class="abs cases"></div>
  <div class="abs cases-title">Case Studies</div>
  <ul class="abs cases-list">
    <li>Management Services</li>
    <li>Consulting Services</li>
    <li>Policy Analysis</li>
    <li>Regulatory Analysis</li>
    <li>Market Assessment</li>
    <li>Program Management</li>
    <li>Regulatory Support</li>
    <li>Risk Assessment</li>
    <li>Market Research</li>
    <li>Custom Training</li>
  </ul>
  <div class="abs hero-photo" role="img" aria-label="Photo of business people shaking hands in an office meeting"></div>
  <div class="abs caption">
    <h2>Lorem Ipsum<br>is simply dummy</h2>
    <p>Many desktop publishing pack-ages and web page editors now use as their default model text, and a search for 'lorem ipsum' will uncover many web sites still in their infancy.</p>
  </div>
  <div class="abs dots"><span></span><span></span><span class="on"></span></div>

  <div class="abs card" style="left:110px">
    <div class="card-head" style="border-color:var(--teal)">Business Technology</div>
    <div class="card-img" role="img" aria-label="Image of a digital binary data tunnel" style="background:linear-gradient(90deg,#0a1e3a,#2a8fd8 60%,#0e2c55)"></div>
    <p class="card-text">Etiam fermentum convallis diam sit amet euismod. Proin euismod tortor ac tellus congue sceler-isque pretium enim volutpat.</p>
    <div class="card-dots"></div><div class="more">Learn more</div>
  </div>
  <div class="abs card" style="left:360px">
    <div class="card-head" style="border-color:var(--green)">Management</div>
    <div class="card-img" role="img" aria-label="Photo of a business team meeting around a laptop" style="background:linear-gradient(90deg,#e9eaec,#3a3d44 50%,#d8d9dc)"></div>
    <p class="card-text">Etiam fermentum convallis diam sit amet euismod. Proin euismod tortor ac tellus congue sceler-isque pretium enim volutpat.</p>
    <div class="card-dots"></div><div class="more">Learn more</div>
  </div>
  <div class="abs card" style="left:611px">
    <div class="card-head" style="border-color:var(--amber)">Market Research</div>
    <div class="card-img" role="img" aria-label="Photo of a hand using a tablet showing charts" style="background:linear-gradient(120deg,#2b3038,#8c8f96 50%,#e3cbb8)"></div>
    <p class="card-text">Etiam fermentum convallis diam sit amet euismod. Proin euismod tortor ac tellus congue sceler-isque pretium enim volutpat.</p>
    <div class="card-dots"></div><div class="more">Learn more</div>
  </div>
  <div class="abs card" style="left:861px">
    <div class="card-head" style="border-color:var(--red)">Sales Analysis</div>
    <div class="card-img" role="img" aria-label="Illustration of colourful 3D bar and pie charts on a tablet" style="background:linear-gradient(#f7f7f7,#e3e6ea)"></div>
    <p class="card-text">Etiam fermentum convallis diam sit amet euismod. Proin euismod tortor ac tellus congue sceler-isque pretium enim volutpat.</p>
    <div class="card-dots"></div><div class="more">Learn more</div>
  </div>

  <div class="abs clients"></div>
  <div class="abs clients-tab">› Just a few of our satisfied customers. <a>View all clients.</a></div>
  <div class="abs client-names">
    <span>Vantora</span><span>Quillsoft</span><span>Lumenar</span><span>ORBIX</span><span>TALVANI</span><span>Drivex</span><span>Homelyn</span>
  </div>

  <div class="abs footer"></div>
  <div class="abs news-title">Join our newsletter</div>
  <p class="abs news-text">and keep informed about special pro-motions and new course titles</p>
  <div class="abs news-form">Enter email
    <span class="news-btn"><svg width="31" height="28" viewBox="0 0 31 28"><path d="M12 7l7 7-7 7" stroke="#fff" stroke-width="2.5" fill="none"/></svg></span>
  </div>
  <div class="abs vrule" style="left:368px"></div>
  <div class="abs vrule" style="left:848px"></div>
  <ul class="abs foot-links">
    <li>Services</li><li>Engaging us</li><li>About Conflict</li><li>Conflict App</li><li>About us</li><li>Contact us</li>
  </ul>
  <div class="abs foot-cases">CASE STUDIES</div>
  <ul class="abs foot-sub" style="left:583px">
    <li>Management Services</li><li>Consulting Services</li><li>Policy Analysis</li><li>Regulatory Analysis</li><li>Market Assessment</li><li>Program Management</li>
  </ul>
  <ul class="abs foot-sub" style="left:725px">
    <li>Regulatory Support</li><li>Risk Assessment</li><li>Market Research</li><li>Custom Training</li>
  </ul>
  <div class="abs office">
    <div class="org">KELBROOK MEDIATION</div>
    <div class="hq">International Head Office</div>
    <span class="sep"></span><br>
    +61 2 5550 1234<br>info@kelbrook.com.au<br>
    <div style="height:9px"></div>
    Level 1, 20 Harbour Lane<br>Sydney AUSTRALIA
  </div>
  <div class="abs hline"></div>
  <div class="abs legal">© Copyright 2013, &nbsp;All Rights Reserved. &nbsp;&nbsp;&nbsp;<a>Terms of Use</a><span class="bar">|</span><a>Privacy Policy</a></div>
  <div class="abs follow">Follow us on:
    <span class="dot" aria-label="Professional network link"></span>
    <span class="dot" aria-label="Microblog link"></span>
    <span class="dot" aria-label="Social network link"></span>
  </div>

</div>
</body>
</html>
```